Poster design for a property rental startup

We need a poster design for a property rental startup.

Size: 60x160cm
Requirements:
1. Simple, clean, modern (and creative if possible)
2. Highlight name Dorvale and the theme (i.e., rental)
3. Ideally one can understand the meaning of the poster (i.e., property rental) even without watching closely or carefully
4. Hopefully it can give people a strong impression so that they can remember it

Info to display:
1. [must] logo + "Dorvale"
2. [must] www.dorvale-example.com
3. [must] Free
4. [must] Reliable listings
5. [must] New online rental experience
6. [optional] The key to your rental

where 3-5 are together (like three bullets)

Industry/Entity Type

Property

```html
<!DOCTYPE html>
<html lang="en">
<head>
<meta charset="utf-8">
<title>Dorvale rental poster</title>
<link href="https://fonts.googleapis.com/css2?family=Arimo:ital,wght@0,400;1,400&family=Libre+Baskerville:wght@700&display=swap" rel="stylesheet">
<style>
  :root {
    --page-bg: #2c4a55;
    --header-top: #101010;
    --header-bottom: #262626;
    --brand-white: #ffffff;
    --brand-cyan: #1fb0e6;
    --panel-grey: #3b3b3b;
    --panel-grey-light: #4b4b4b;
    --bullet-blue: #2e8fd6;
    --url-blue: #3a8fd0;
    --band-black: #151515;
    --footer-top: #c8f1f8;
    --footer-bottom: #a7e2ee;
    --footer-text: #2a86c6;
  }
  * { margin: 0; padding: 0; box-sizing: border-box; }
  html, body {
    width: 700px; height: 1200px; overflow: hidden;
    background: var(--page-bg);
  }
  .poster {
    position: absolute; left: 164px; top: 64px;
    width: 401px; height: 1068px;
    background: var(--header-bottom);
    overflow: hidden;
    font-family: "Arimo", Arial, sans-serif;
  }
  .masthead {
    position: absolute; left: 0; top: 0; width: 100%; height: 200px;
    background: linear-gradient(var(--header-top), var(--header-bottom));
    text-align: center;
  }
  .brand-name {
    position: absolute; left: 0; right: 0; top: 26px;
    font-family: "Libre Baskerville", Georgia, serif; font-weight: 700;
    font-size: 46px; line-height: 56px; color: var(--brand-white); letter-spacing: 0.5px;
    white-space: nowrap;
  }
  .brand-rule {
    position: absolute; left: 80px; right: 74px; top: 87px;
    height: 2px; background: var(--brand-cyan);
  }
  .brand-tagline {
    position: absolute; left: 0; right: 0; top: 90px;
    font-size: 34px; line-height: 40px; letter-spacing: 10px; color: var(--brand-cyan);
    white-space: nowrap;
  }
  .photo-terrace {
    position: absolute; left: 9px; top: 136px; width: 383px; height: 286px;
    border-radius: 42px;
    background: linear-gradient(160deg, #a9c9e6 0%, #b6643f 35%, #8a4a33 60%, #d9d3c8 82%, #3f5a2a 100%);
  }
  .benefits {
    position: absolute; left: 0; top: 422px; width: 100%; height: 198px;
    background: var(--panel-grey);
  }
  .benefits svg.curves { position: absolute; left: 0; top: 0; }
  .benefit-list { position: absolute; left: 78px; top: 14px; list-style: none; }
  .benefit {
    position: relative; padding-left: 76px; margin-bottom: 16px;
    color: var(--brand-white); font-size: 24px; line-height: 34px;
    white-space: nowrap;
  }
  .benefit svg { position: absolute; left: 2px; top: 2px; }
  .photo-apartments {
    position: absolute; left: 0; top: 620px; width: 100%; height: 266px;
    background: linear-gradient(180deg, #6f8fb3 0%, #c9d3de 30%, #a05a42 55%, #7a4536 75%, #2f4a28 100%);
  }
  .web-band {
    position: absolute; left: 0; top: 886px; width: 100%; height: 80px;
    background: var(--band-black);
    display: flex; align-items: center; justify-content: center; gap: 12px;
  }
  .web-band svg { flex: none; }
  .web-address {
    font-style: italic; font-size: 23px; line-height: 30px; color: var(--url-blue);
    white-space: nowrap;
  }
  .footer {
    position: absolute; left: 0; top: 966px; width: 100%; height: 102px;
    background: linear-gradient(var(--footer-top), var(--footer-bottom));
    display: flex; align-items: center; justify-content: center;
  }
  .footer-line {
    font-size: 25px; line-height: 30px; color: var(--footer-text);
    white-space: nowrap;
  }
</style>
</head>
<body>
<div class="poster">
  <header class="masthead">
    <div class="brand-name">Dorvale</div>
    <div class="brand-rule"></div>
    <div class="brand-tagline">rental</div>
  </header>

  <div class="photo-terrace" role="img" aria-label="Photo of a row of red-brick Victorian terraced houses with white bay windows under a blue sky"></div>

  <section class="benefits">
    <svg class="curves" width="401" height="198" viewBox="0 0 401 198" aria-hidden="true">
      <path d="M0 40 Q200 -10 401 30 L401 198 L0 198 Z" fill="var(--panel-grey-light)" opacity="0.5"/>
      <path d="M0 198 Q180 60 401 70 L401 198 Z" fill="var(--panel-grey-light)" opacity="0.6"/>
    </svg>
    <ul class="benefit-list">
      <li class="benefit">
        <svg width="30" height="30" viewBox="0 0 30 30" aria-hidden="true"><circle cx="15" cy="15" r="14" fill="var(--bullet-blue)"/><path d="M8 15 L13 20 L22 10" stroke="#fff" stroke-width="3" fill="none"/></svg>
        Free
      </li>
      <li class="benefit">
        <svg width="30" height="30" viewBox="0 0 30 30" aria-hidden="true"><circle cx="15" cy="15" r="14" fill="var(--bullet-blue)"/><path d="M8 15 L13 20 L22 10" stroke="#fff" stroke-width="3" fill="none"/></svg>
        Reliable listings
      </li>
      <li class="benefit">
        <svg width="30" height="30" viewBox="0 0 30 30" aria-hidden="true"><circle cx="15" cy="15" r="14" fill="var(--bullet-blue)"/><path d="M8 15 L13 20 L22 10" stroke="#fff" stroke-width="3" fill="none"/></svg>
        New online rental<br>experience
      </li>
    </ul>
  </section>

  <div class="photo-apartments" role="img" aria-label="Photo of a modern red-brick apartment block with balconies against a cloudy sky, trees at its base"></div>

  <div class="web-band">
    <svg width="40" height="40" viewBox="0 0 42 42" aria-hidden="true" fill="none" stroke="#fff" stroke-width="2">
      <circle cx="21" cy="21" r="19"/>
      <ellipse cx="21" cy="21" rx="8" ry="19"/>
      <line x1="21" y1="2" x2="21" y2="40"/>
      <line x1="2" y1="21" x2="40" y2="21"/>
      <path d="M5 11 H37 M5 31 H37"/>
    </svg>
    <div class="web-address">www.dorvale-example.com</div>
  </div>

  <footer class="footer">
    <div class="footer-line">The key to your rental</div>
  </footer>
</div>
</body>
</html>
```